Time for a new business card design

We need a new business card design for Torvel Furniture Rentals based in Australia. www.torvel-example.com.au. We specialise in providing furniture rentals for home staging, corporate relocations events and product launches etc. We would like to see designs that include our logo on the front of the card with all the standard contact details as well as having a realy nice image on the back with a list of our services we offer. Our logo is red and this cannot change. Were looking for a pallet of red and white with maybe a splash of grey. The final design should communication organised & stylish. We are in the process of finalising our new website and would like the card design to compliment this as well

Industry/Entity Type

Communication

Requirements
Must have
• Square corners
logo
name, title, email, phone, address
image on back of card with space for list of services we offer
Services:
•Furniture and appliance rental
•Property styling
•Events and functions
•Office furniture rental

The card must be landscape.
The image is to appear on the back of the card only.

```html
<!DOCTYPE html>
<html lang="en">
<head>
<meta charset="utf-8">
<title>Torvel Furniture Rentals – Business Card</title>
<link rel="stylesheet" href="https://fonts.googleapis.com/css2?family=Questrial&family=Lato:ital,wght@1,400;1,700&display=swap">
<style>
  :root {
    --brand-red: #b8262b;
    --band-grey: #7b7b7b;
    --text-grey: #6e6e6e;
    --card-white: #ffffff;
    --backdrop: #e4e7e8;
    --sky-blue: #5fa3d8;
    --linen: #f1f1f1;
  }
  * { box-sizing: border-box; margin: 0; padding: 0; }
  html, body {
    width: 1200px;
    height: 960px;
    overflow: hidden;
    background: var(--backdrop);
  }
  .sheet {
    position: relative;
    width: 1200px;
    height: 960px;
  }
  .card {
    position: absolute;
    left: 320px;
    width: 560px;
    height: 320px;
    background: var(--card-white);
    box-shadow: 0 4px 16px rgba(0,0,0,0.15);
    overflow: hidden;
  }
  .card--front { top: 110px; }
  .card--back  { top: 530px; }

  /* Front */
  .brand {
    position: absolute;
    top: 52px;
    left: 0;
    width: 100%;
    text-align: center;
    font-family: "Questrial", sans-serif;
    font-size: 46px;
    color: var(--brand-red);
    letter-spacing: -0.5px;
  }
  .name-band {
    position: absolute;
    top: 160px;
    left: 0;
    width: 100%;
    height: 56px;
    background: var(--band-grey);
    display: flex;
    align-items: center;
    justify-content: center;
    font-family: "Questrial", sans-serif;
    color: var(--card-white);
  }
  .name-band .person-name { font-size: 25px; }
  .name-band .person-title { font-size: 16px; margin-left: 6px; }
  .contact {
    position: absolute;
    top: 238px;
    left: 0;
    width: 100%;
    text-align: center;
    font-family: "Questrial", sans-serif;
    color: var(--text-grey);
    line-height: 1.35;
  }
  .contact .contact-line { font-size: 15px; }
  .contact .contact-line span + span { margin-left: 26px; }
  .contact .address { font-size: 15.5px; }
  .contact .website { font-size: 14px; font-weight: 700; font-family: "Lato", sans-serif; font-style: normal; }

  /* Back */
  .back-photo {
    position: absolute;
    inset: 0;
    background:
      linear-gradient(180deg, var(--sky-blue) 0%, #9cc6e6 14%, #dfe3e6 22%, #eeeeee 55%, var(--linen) 100%);
  }
  .services {
    position: absolute;
    left: 40px;
    right: 40px;
    bottom: 38px;
    text-align: center;
    font-family: "Lato", sans-serif;
    font-style: italic;
    font-size: 14px;
    color: var(--brand-red);
  }
  .services .rule {
    display: block;
    height: 1px;
    background: var(--brand-red);
    margin: 3px 0;
  }
  .services .services-line span + span::before {
    content: "•";
    margin: 0 6px;
    font-style: normal;
  }
</style>
</head>
<body>
<main class="sheet">
  <section class="card card--front" aria-label="Front of business card">
    <div class="brand">torvel furniture rentals</div>
    <div class="name-band">
      <span class="person-name">Name Surname</span>
      <span class="person-title">/ Operation Manager</span>
    </div>
    <div class="contact">
      <p class="contact-line"><span>T: 1800 55 01 23</span><span>E: info@torvel-example.com.au</span></p>
      <p class="address">Harbour Lane - Bay Rise, PO 375 - City, Country</p>
      <p class="website">www.torvel-example.com.au</p>
    </div>
  </section>

  <section class="card card--back" aria-label="Back of business card">
    <div class="back-photo" role="img" aria-label="Photo of a bright styled bedroom with patterned red cushions, a lamp and an ocean view through the window"></div>
    <div class="services">
      <p class="services-line"><span>Furniture and appliance rental</span><span>Property styling</span><span>Events and functions</span></p>
      <span class="rule"></span>
      <p class="services-line"><span>Office furniture rental</span></p>
      <span class="rule"></span>
    </div>
  </section>
</main>
</body>
</html>
```